Supplement Company Needs a Protein Powder Pouch Design

We are looking for a modern and fresh design for our 500g pouches of protein powder as our current design is not eye catching or exciting enough.

This new design will be printed on both sides of a 178mm x 280mm x 101mm pouch.

We have 4 flavours. These are Banana Ice Cream, Chocolate Deluxe, Strawberries & Cream and Vanilla Ice Cream.

Industry/Entity Type

Supplement

Requirements
Must have
• Attractive and eye catching front and space for all the nutritional information and ingredients on the back.

Must clearly state 'food supplement' somewhere on the front of the pouch.
Nice to have
• Our logo is attached.
Should not have
• No health claims as these are not allowed in the UK

```html
<!DOCTYPE html>
<html lang="en">
<head>
<meta charset="utf-8">
<title>BRISK Supplements – Chocolate Deluxe Protein Powder Pouch</title>
<link href="https://fonts.googleapis.com/css2?family=Montserrat:wght@700;800&family=Roboto+Condensed:wght@400;700&display=swap" rel="stylesheet">
<style>
  :root {
    --bg: #ffffff;
    --pouch-white: #fbfbfb;
    --tan-dark: #c5825a;
    --tan-light: #e8b38f;
    --cream: #f1ece8;
    --ink: #2a2a2c;
    --maroon: #6e1f14;
    --maroon-mid: #8a3222;
    --choc-dark: #5b3022;
    --choc-light: #a86a52;
    --panel: #ffffff;
    --label-grey: #b7a79a;
  }
  * { box-sizing: border-box; margin: 0; padding: 0; }
  html, body { width: 1200px; height: 1028px; overflow: hidden; background: var(--bg); }
  .canvas { position: relative; width: 1200px; height: 1028px; }

  .pouch {
    position: absolute; top: 142px; width: 501px; height: 701px;
    background: var(--pouch-white);
    border-radius: 6px 6px 4px 4px;
    box-shadow: 0 2px 10px rgba(0,0,0,.08);
    overflow: hidden;
  }
  .pouch--front { left: 76px; }
  .pouch--back { left: 630px; }

  .zip-line {
    position: absolute; left: 24px; right: 24px; top: 102px; height: 4px;
    background: linear-gradient(#e9e9e9, #f7f7f7); border-radius: 2px;
  }

  .brand-name, .brand-sub {
    position: absolute; left: 0; right: 0; text-align: center; color: var(--ink);
    font-family: "Montserrat", sans-serif; font-weight: 800; line-height: 1; white-space: nowrap;
  }
  .brand-name { letter-spacing: -2px; }

  .tan-band {
    position: absolute; left: 10px; right: 10px; bottom: 0;
    background: linear-gradient(100deg, var(--tan-dark) 0%, #d39570 55%, var(--tan-light) 100%);
  }

  .title-line {
    position: absolute; font-family: "Montserrat", sans-serif; font-weight: 800;
    line-height: 1; white-space: nowrap; color: var(--cream);
  }
  .title-line--main { letter-spacing: -1px; }
  .title-line--dark { color: var(--ink); }

  .flavour-band {
    position: absolute; left: 10px; right: 10px;
    background: linear-gradient(90deg, var(--maroon) 0%, var(--maroon-mid) 50%, var(--maroon) 100%);
  }
  .flavour-band__text {
    position: absolute; color: var(--cream); white-space: nowrap;
    font-family: "Montserrat", sans-serif; font-weight: 800;
  }

  .product-art {
    position: absolute; border-radius: 6px;
    background: linear-gradient(135deg, var(--choc-light), var(--choc-dark));
    box-shadow: 4px 6px 10px rgba(0,0,0,.25);
  }

  .net-weight {
    position: absolute; left: 114px; top: 676px; color: var(--label-grey);
    font-family: "Roboto Condensed", sans-serif; font-weight: 700; font-size: 13px;
  }

  .nutrition {
    position: absolute; left: 30px; top: 519px; width: 442px; height: 50px;
    background: var(--panel); border-radius: 3px; display: flex;
    font-family: "Roboto Condensed", sans-serif; color: var(--ink); font-size: 5.2px; padding: 3px;
  }
  .nutrition__intro { width: 78px; padding-right: 3px; border-right: 1px solid var(--ink); position: relative; }
  .nutrition__heading { font-weight: 700; font-size: 6.8px; border-bottom: 1px solid var(--ink); padding-bottom: 1px; }
  .nutrition__desc { font-weight: 700; margin-top: 2px; line-height: 1.25; }
  .nutrition__weight { position: absolute; bottom: 1px; font-weight: 700; font-size: 6.6px; }
  .nutrition__col { width: 68px; padding: 0 3px; border-right: 1px solid var(--ink); }
  .nutrition__col-head { font-weight: 700; font-size: 5.4px; border-bottom: 1px solid var(--ink); padding-bottom: 1px; margin-bottom: 1px; }
  .nutrition__row { display: flex; justify-content: space-between; border-bottom: 1px solid #999; line-height: 7.2px; }
  .nutrition__row--sub span:first-child { font-style: italic; padding-left: 3px; }
  .nutrition__cals { flex: 1; text-align: center; font-weight: 700; padding-top: 1px; }
  .nutrition__cals-label { font-size: 6.2px; line-height: 1; }
  .nutrition__cals-value { font-size: 19px; line-height: 1; }
  .nutrition__cals-serv { font-size: 5.6px; border-top: 1px solid var(--ink); margin-top: 2px; padding-top: 1px; }

  .info {
    position: absolute; left: 26px; right: 26px; top: 580px;
    font-family: "Roboto Condensed", sans-serif; font-size: 6.4px; line-height: 1.06; color: #4a3126;
  }
  .info p { margin-bottom: 3px; }
  .info strong { font-weight: 700; }
  .info__footer { display: flex; justify-content: space-between; margin-top: 4px; }
</style>
</head>
<body>
<main class="canvas">

  <section class="pouch pouch--front">
    <div class="zip-line"></div>
    <span class="brand-name" style="top:192px;font-size:96px">BRISK</span>
    <span class="brand-sub" style="top:293px;font-size:17px;letter-spacing:16px;padding-left:16px">SUPPLEMENTS</span>
    <div class="tan-band" style="top:326px"></div>
    <h1>
      <span class="title-line" style="top:334px;left:106px;font-size:28px">FOOD SUPPLEMENT</span>
      <span class="title-line title-line--main" style="top:362px;left:106px;font-size:66px">PROTEIN</span>
      <span class="title-line title-line--main title-line--dark" style="top:420px;left:106px;font-size:66px">POWDER</span>
    </h1>
    <div class="flavour-band" style="top:514px;height:63px">
      <p class="flavour-band__text" style="top:9px;left:98px;font-size:21px;line-height:23px">CHOCOLATE<br>DELUXE FLAVOUR</p>
    </div>
    <div class="product-art" role="img" aria-label="Broken squares of milk chocolate" style="left:322px;top:552px;width:135px;height:115px"></div>
    <p class="net-weight">Net Weight: 500g</p>
  </section>

  <section class="pouch pouch--back">
    <div class="zip-line"></div>
    <span class="brand-name" style="top:191px;font-size:84px">BRISK</span>
    <span class="brand-sub" style="top:274px;font-size:15px;letter-spacing:13px;padding-left:13px">SUPPLEMENTS</span>
    <div class="tan-band" style="top:298px"></div>
    <h2>
      <span class="title-line" style="top:309px;left:127px;font-size:24px">FOOD SUPPLEMENT</span>
      <span class="title-line title-line--main" style="top:334px;left:125px;font-size:56px">PROTEIN</span>
      <span class="title-line title-line--main title-line--dark" style="top:384px;left:125px;font-size:56px">POWDER</span>
    </h2>
    <div class="flavour-band" style="top:447px;height:54px">
      <p class="flavour-band__text" style="top:6px;left:117px;font-size:18px;line-height:19px">CHOCOLATE<br>DELUXE FLAVOUR</p>
    </div>
    <div class="product-art" role="img" aria-label="Broken squares of milk chocolate" style="left:322px;top:438px;width:148px;height:78px"></div>

    <div class="nutrition">
      <div class="nutrition__intro">
        <div class="nutrition__heading">Nutritional Information</div>
        <div class="nutrition__desc">Chocolate flavour<br>protein food supplement<br>with sweetener.</div>
        <div class="nutrition__weight">Net Weight: 500g</div>
      </div>
      <div class="nutrition__col">
        <div class="nutrition__col-head">Typical values per 30g</div>
        <div class="nutrition__row"><span>Energy</span><span>489kj</span></div>
        <div class="nutrition__row"><span></span><span>117kcals</span></div>
        <div class="nutrition__row"><span>Fat</span><span>1.8g</span></div>
        <div class="nutrition__row nutrition__row--sub"><span>of which saturates</span><span>0.03g</span></div>
      </div>
      <div class="nutrition__col">
        <div class="nutrition__col-head">Typical values per 30g</div>
        <div class="nutrition__row"><span>Carbohydrate</span><span>4.2g</span></div>
        <div class="nutrition__row nutrition__row--sub"><span>of which sugars</span><span>3g</span></div>
        <div class="nutrition__row"><span>Protein</span><span>21g</span></div>
        <div class="nutrition__row"><span>Salt</span><span>0.2g</span></div>
      </div>
      <div class="nutrition__col">
        <div class="nutrition__col-head">Typical values per 100g</div>
        <div class="nutrition__row"><span>Energy</span><span>1630kj</span></div>
        <div class="nutrition__row"><span></span><span>390kcals</span></div>
        <div class="nutrition__row"><span>Fat</span><span>6g</span></div>
        <div class="nutrition__row nutrition__row--sub"><span>of which saturates</span><span>0.1g</span></div>
      </div>
      <div class="nutrition__col">
        <div class="nutrition__col-head">Typical values per 30g</div>
        <div class="nutrition__row"><span>Carbohydrate</span><span>14g</span></div>
        <div class="nutrition__row nutrition__row--sub"><span>of which sugars</span><span>10g</span></div>
        <div class="nutrition__row"><span>Protein</span><span>70g</span></div>
        <div class="nutrition__row"><span>Salt</span><span>0.8g</span></div>
      </div>
      <div class="nutrition__cals">
        <div class="nutrition__cals-label">Calories per<br>30g serving:</div>
        <div class="nutrition__cals-value">117</div>
        <div class="nutrition__cals-serv">16 servings</div>
      </div>
    </div>

    <div class="info">
      <p><strong>SUGGESTED USE:</strong> We recommend using one the two servings of 30g per day. One serving is one level scoop (a scoop is inside this pouch). Mix one level scoop with at least 200 ml of cold water. Do not exceed recommended daily dose.</p>
      <p><strong>STORAGE INFORMATION:</strong> Store in cool and dry place. Reseal this pouch after each use. Keep out of sight and reach of children.</p>
      <p><strong>INGREDIENTS:</strong> Protein Blend (<strong>Soya</strong> Protein Isolate, Whey Protein Concentrate (<strong>Milk</strong>), <strong>Milk</strong> Protein)(70%), Acetyl-Carnitine (500mg per 100g), Acai Berry 4:1 Extract (400mg per 100g), Green Tea Extract (400mg per 100g), Conjugated Linoleic Acid Powder (50mg per 100g), Flavouring, Fat Reduced Cocoa Powder (10%), Thickener (Xanthan Gum), Sweetener (Sucralose).<br>Manufactured in the UK with EU protein powder (Germany) and non-EU cocoa powder (Ghana).</p>
      <p><strong>ALLERGEN INFORMATION:</strong> For allergens, see ingredients in <strong>bold</strong>. May also contain cereal containing gluten, nuts, egg, peanuts.</p>
      <p><strong>CAUTION:</strong> Food supplements should not be used as a substitute for varied and healthy lifestyle. This product is not recommended for use by pregnant or lactating women. If you are taking any medications or are under medical supervision, you should consult with your health care professional before use, taking into consideration other supplements and medications you consume. This product is not intended for use by persons under age of 18.</p>
      <div class="info__footer">
        <span><strong>BRISK Supplements Limited,</strong> Mill Lane, Eastbrook, Kentshire, EX12 9ZZ.</span>
        <span>Best before: See back of pouch</span>
      </div>
    </div>
  </section>

</main>
</body>
</html>
```